Stationary/business card design for Harborline Building Partners
Harborline Building Partners
Stationary/business card design for Harborline Building Partners - Consulting
Creative Brief
Use specific fonts
Up to designer. Can be different from logo if that looks good.
Simple
Clara T Revanski
Director - Business Development & Support
3870 Wexmoor Avenue - Suite 2C Rochester, NY 14618
clara.revanski@hbpworkline.com
www.HBPworkline.com
The back of the business card will have some of what we do on there, for example: GIS, Drafting, Master Data. I haven't written that up yet.

```html
<!DOCTYPE html>
<html lang="en">
<head>
<meta charset="utf-8">
<title>Harborline Building Partners — Stationery Set</title>
<link rel="stylesheet" href="https://fonts.googleapis.com/css2?family=Cinzel:wght@600&family=Open+Sans:wght@400;600&display=swap">
<style>
  :root {
    --bg-light: #b9b9b9;
    --bg-dark: #8a8a8a;
    --paper: #ffffff;
    --green: #2aa84a;
    --green-dark: #1d7f37;
    --ink: #5a5a5a;
    --faint: #ececec;
    --name-font: "Cinzel", Georgia, serif;
    --body-font: "Open Sans", Arial, sans-serif;
  }
  * { box-sizing: border-box; margin: 0; padding: 0; }
  html, body { width: 1200px; height: 469px; overflow: hidden; }
  body {
    position: relative;
    background: radial-gradient(ellipse at 55% 45%, var(--bg-light) 0%, var(--bg-dark) 100%);
    font-family: var(--body-font);
    color: var(--ink);
  }
  .sheet {
    position: absolute;
    background: var(--paper);
    box-shadow: 0 2px 6px rgba(0,0,0,.25);
    overflow: hidden;
  }
  .brand {
    display: flex; align-items: center; gap: 3px;
    font-family: var(--name-font); font-weight: 600; color: var(--green);
    line-height: 1.05; white-space: nowrap;
  }
  .brand-square { display: inline-block; background: var(--green); flex: none; }
  .faint-name {
    position: absolute; left: 0; right: 0; text-align: center;
    font-family: var(--name-font); font-weight: 600; color: var(--faint);
    line-height: 1.1;
  }
  .tiny { font-size: 4px; line-height: 1.45; white-space: nowrap; }

  /* Business cards */
  .card { left: 34px; width: 125px; height: 67px; border-radius: 3px; }
  .card-front { top: 154px; padding: 8px 7px; }
  .card-front .brand { font-size: 5px; }
  .card-front .brand-square { width: 5px; height: 5px; }
  .card-front .person { margin-top: 6px; display: flex; justify-content: space-between; gap: 4px; }
  .card-front .tiny { font-size: 3.2px; }
  .card-front .person-name { font-size: 4.5px; font-weight: 600; color: var(--green-dark); margin-bottom: 1px; }
  .card-front .person-web { text-align: right; padding-top: 6px; }
  .card-front .person-email { margin-top: 4px; color: var(--green-dark); }
  .card-back { top: 241px; }
  .card-back .faint-name { top: 22px; font-size: 9px; }
  .card-back .services { position: absolute; bottom: 7px; left: 0; right: 0; text-align: center; color: var(--green); }

  /* Letterheads */
  .letterhead { top: 34px; width: 220px; height: 399px; }
  .letterhead-one { left: 269px; }
  .letterhead-two { left: 525px; }
  .letterhead .brand { position: absolute; top: 10px; font-size: 8px; }
  .letterhead-one .brand { left: 50%; transform: translateX(-50%); }
  .letterhead-two .brand { left: 10px; font-size: 6.5px; }
  .letterhead .brand-square { width: 7px; height: 7px; }
  .letterhead-two .brand-square { width: 6px; height: 6px; }
  .letterhead .contact { position: absolute; top: 10px; right: 10px; text-align: right; }
  .letterhead .contact .tiny { font-size: 3.3px; }
  .letterhead .faint-name { top: 190px; font-size: 15px; }
  .letterhead .rule-thin { position: absolute; left: 0; right: 0; bottom: 18px; height: 2px; background: var(--green); }
  .letterhead .rule-band { position: absolute; left: 0; right: 0; bottom: 7px; height: 7px; background: var(--green); }
  .letterhead .footer-line { position: absolute; left: 0; right: 0; bottom: 9px; text-align: center; color: #fff; font-size: 3.5px; }

  /* Envelopes */
  .envelope { left: 849px; width: 322px; }
  .envelope-front { top: 63px; height: 153px; }
  .envelope-front .brand { position: absolute; top: 12px; left: 12px; font-size: 8px; }
  .envelope-front .brand-square { width: 7px; height: 7px; }
  .envelope-front .return { position: absolute; top: 24px; left: 12px; }
  .envelope-front .faint-name { top: 60px; left: 150px; right: 12px; font-size: 12px; }
  .envelope-back { top: 236px; height: 156px; }
  .envelope-back svg { position: absolute; inset: 0; }
  .envelope-back .brand { position: absolute; left: 50%; transform: translateX(-50%); font-size: 8px; }
  .envelope-back .brand-square { width: 7px; height: 7px; }
  .flap-brand { top: 21px; color: #fff !important; }
  .flap-brand .brand-square { background: #fff; }
  .seal-brand { top: 98px; }
</style>
</head>
<body>

  <section class="sheet card card-front" aria-label="Business card front">
    <div class="brand"><span class="brand-square"></span>Harborline Building Partners</div>
    <div class="person">
      <div>
        <div class="person-name">Clara T Revanski</div>
        <div class="tiny">Director - Business Development</div>
        <div class="tiny">&amp; Support</div>
        <div class="tiny">3870 Wexmoor Avenue - Suite 2C</div>
        <div class="tiny">Rochester, NY 14618</div>
      </div>
      <div class="person-web">
        <div class="tiny">www.HBPworkline.com</div>
        <div class="tiny">Skype: pelliard</div>
      </div>
    </div>
    <div class="tiny person-email">clara.revanski@hbpworkline.com</div>
  </section>

  <section class="sheet card card-back" aria-label="Business card back">
    <div class="faint-name">Harborline</div>
    <div class="tiny services">GIS · Drafting · Master Data</div>
  </section>

  <section class="sheet letterhead letterhead-one" aria-label="Letterhead, first page">
    <div class="brand"><span class="brand-square"></span>Harborline Building Partners</div>
    <div class="faint-name">Harborline</div>
    <div class="rule-thin"></div>
    <div class="rule-band"></div>
    <div class="footer-line">3870 Wexmoor Avenue - Suite 2C Rochester, NY 14618 · www.HBPworkline.com</div>
  </section>

  <section class="sheet letterhead letterhead-two" aria-label="Letterhead, second page">
    <div class="brand"><span class="brand-square"></span>Harborline Building Partners</div>
    <div class="contact">
      <div class="tiny">3870 Wexmoor Avenue - Suite 2C</div>
      <div class="tiny">Rochester, NY 14618</div>
      <div class="tiny">www.HBPworkline.com</div>
    </div>
    <div class="faint-name">Harborline</div>
    <div class="rule-thin"></div>
    <div class="rule-band"></div>
  </section>

  <section class="sheet envelope envelope-front" aria-label="Envelope front">
    <div class="brand"><span class="brand-square"></span>Harborline Building Partners</div>
    <div class="return">
      <div class="tiny">3870 Wexmoor Avenue - Suite 2C</div>
      <div class="tiny">Rochester, NY 14618</div>
    </div>
    <div class="faint-name">Harborline</div>
  </section>

  <section class="sheet envelope envelope-back" aria-label="Envelope back">
    <svg width="322" height="156" viewBox="0 0 322 156">
      <polygon points="0,0 322,0 322,22 161,52 0,22" fill="var(--green)"/>
      <polyline points="0,70 161,115 322,70" fill="none" stroke="#d6d6d6" stroke-width="1"/>
      <line x1="0" y1="156" x2="140" y2="100" stroke="#e2e2e2" stroke-width="1"/>
      <line x1="322" y1="156" x2="182" y2="100" stroke="#e2e2e2" stroke-width="1"/>
    </svg>
    <div class="brand flap-brand"><span class="brand-square"></span>Harborline</div>
    <div class="brand seal-brand"><span class="brand-square"></span>Harborline</div>
  </section>

</body>
</html>
```